Cellar Legacies, a definitive reference book on port

My husband has just finished writing a big book on Vintage Port. We need a hardcover book flap design for this book that is impressively huge. It's taken 10 years to research and write. It's 650 pages, interior is A4, exterior 4mm larger, and weighs nearly 3 kilos. It's a special book for people in the wine and port industry, as well as for someone who loves to drink Vintage Port. It can be a beautiful coffeetable book too.

The book is mainly about port and its declared vintages. It's also about the history of port, who drank it, when, how, where, who bought it, for how much, and the port houses are also described in detail.

The wine expert Gerald Thornwick wrote a book about vintage wine in 2002, and my husband would like to have a similar cover for his book. (A photo attached in files). I've attached other photos to give the designers an idea of the look and feel of the 'port culture', as well as photos of the typeface that my husband will be using for the inside hardcover.

Target Market(s)

Wine and port industry. Wine aficionados.

Industry/Entity Type

Winery

Font styles to use
Sans Serif
Script

Colors
ec1f27
1b1b1b
474747
333333
5c5c5c
faa54b

Requirements
Must have
• Book Cover must have Title: "Cellar Legacies" and "R. T. K. Hollister" (files attached to show proper typeface). One of the files is a flap jacket book cover that my husband designed himself. We're looking for more design ideas, and that pdf is a close winner to what he wants.
Nice to have
• illustration or painting of port glasses, or grapes, or similar. Dark colors, especially port wine, deep red wine colors. Gold writing, black writing, with red/berry/maroon accents. Luxury, elegance, has a masculine edge, traditional, but not too old-school and boring (like grandpa). Textures that are including with the culture of drinking vintage port are leather, velvet, cigar, wood, marble, winter, fireplaces. This sounds quite heavy, but it also should be simple and clean. I hope this isn't too confusing. Thanks!
Should not have
• Bright colors, playfulness.

```html
<!DOCTYPE html>
<html lang="en">
<head>
<meta charset="utf-8">
<title>Cellar Legacies — Hardcover Jacket</title>
<link href="https://fonts.googleapis.com/css2?family=Cinzel:wght@400&display=swap" rel="stylesheet">
<style>
  :root {
    --backdrop: #8c8b8c;
    --board: #151515;
    --board-edge: #1d1d1d;
    --gold: #9c8a1e;
  }
  * { margin: 0; padding: 0; box-sizing: border-box; }
  html, body {
    width: 1200px;
    height: 854px;
    overflow: hidden;
    background: var(--backdrop);
  }
  .jacket {
    position: relative;
    width: 1200px;
    height: 854px;
  }
  .front-cover {
    position: absolute;
    left: 250px;
    top: 57px;
    width: 520px;
    height: 740px;
    background: radial-gradient(ellipse at 50% 35%, #1c1c1c 0%, var(--board) 70%);
    border: 1px solid var(--board-edge);
  }
  .cover-frame {
    position: absolute;
    inset: 15px;
    border: 1px solid var(--gold);
  }
  .ornament {
    position: absolute;
    left: 100px;
    width: 320px;
    height: 90px;
  }
  .ornament-top { top: 84px; }
  .ornament-bottom { top: 256px; }
  .title-rule {
    position: absolute;
    left: 79px;
    width: 362px;
    height: 2px;
    background: var(--gold);
  }
  .title-rule.upper { top: 178px; }
  .title-rule.lower { top: 251px; }
  .title-rule::before, .title-rule::after {
    content: "";
    position: absolute;
    top: -3px;
    width: 8px;
    height: 8px;
    border: 1px solid var(--gold);
    border-radius: 50%;
  }
  .title-rule::before { left: -6px; }
  .title-rule::after { right: -6px; }
  .cover-title {
    position: absolute;
    top: 194px;
    left: 0;
    right: 0;
    text-align: center;
    font-family: "Cinzel", serif;
    font-weight: 400;
    font-size: 34px;
    letter-spacing: 1.5px;
    text-transform: uppercase;
    color: var(--gold);
    line-height: 1.2;
  }
  .cover-subtitle {
    position: absolute;
    top: 392px;
    left: 0;
    right: 0;
    text-align: center;
    font-family: "Cinzel", serif;
    font-size: 10px;
    line-height: 12px;
    letter-spacing: 0.2px;
    color: var(--gold);
  }
  .cover-author {
    position: absolute;
    top: 617px;
    left: 0;
    right: 0;
    text-align: center;
    font-family: "Cinzel", serif;
    font-size: 22px;
    letter-spacing: 0.5px;
    color: var(--gold);
  }
  .spine {
    position: absolute;
    left: 835px;
    top: 59px;
    width: 97px;
    height: 738px;
    background: linear-gradient(90deg, #1d1d1d 0%, var(--board) 40%, #111 100%);
    border: 1px solid var(--board-edge);
  }
  .spine-title, .spine-author {
    position: absolute;
    left: 50%;
    transform: translateX(-50%);
    writing-mode: vertical-rl;
    font-family: "Cinzel", serif;
    color: var(--gold);
    white-space: nowrap;
    text-transform: uppercase;
  }
  .spine-title {
    top: 46px;
    font-size: 32px;
    letter-spacing: 2px;
  }
  .spine-author {
    top: 492px;
    font-size: 20px;
    letter-spacing: 0.5px;
  }
</style>
</head>
<body>
  <main class="jacket">
    <section class="front-cover">
      <div class="cover-frame"></div>

      <svg class="ornament ornament-top" viewBox="0 0 320 90" role="img" aria-label="Gold scrollwork flourish above the title">
        <defs>
          <radialGradient id="flourishGlowTop" cx="50%" cy="70%" r="60%">
            <stop offset="0%" stop-color="#9c8a1e" stop-opacity="0.45"/>
            <stop offset="100%" stop-color="#9c8a1e" stop-opacity="0.08"/>
          </radialGradient>
        </defs>
        <rect x="0" y="0" width="320" height="90" rx="40" fill="url(#flourishGlowTop)"/>
      </svg>

      <div class="title-rule upper"></div>
      <h1 class="cover-title">Cellar Legacies</h1>
      <div class="title-rule lower"></div>

      <svg class="ornament ornament-bottom" viewBox="0 0 320 90" role="img" aria-label="Gold scrollwork flourish below the title">
        <defs>
          <radialGradient id="flourishGlowBottom" cx="50%" cy="30%" r="60%">
            <stop offset="0%" stop-color="#9c8a1e" stop-opacity="0.45"/>
            <stop offset="100%" stop-color="#9c8a1e" stop-opacity="0.08"/>
          </radialGradient>
        </defs>
        <rect x="0" y="0" width="320" height="90" rx="40" fill="url(#flourishGlowBottom)"/>
      </svg>

      <p class="cover-subtitle">A RECORD OF DECLARED PORT VINTAGES, FROM THE FIRST HARVESTS,<br>DOCUMENTED, DETAILED AND COMPLETE</p>
      <p class="cover-author">R. T. K. HOLLISTER</p>
    </section>

    <aside class="spine">
      <span class="spine-title">Cellar Legacies</span>
      <span class="spine-author">R. T. K. Hollister</span>
    </aside>
  </main>
</body>
</html>
```